BRAYLEN AT HEARTH, LLC Webpage portfolio

I want to create a Website that allows my potential clients to browse my Skilled work via before and after photos. I want the website to enhance the work that I provide and potentially drive new business, or at least solidify my work.
I also do 3D CAD and Modeling of New Spaces and it would be nice to show some of that work from pencil design to 3D modeling, which I feel may help give me more clients.

The website needs to show a solid carpenter/company with the skills to get any project completed.

Types of Jobs - Custom Carpentry & Finishes, Kitchens, Baths, Basements, Decks, Porches, Whole House Renovation - Skilled Craftsmanship (Hardwood Flooring, Floor and Wall Tile) and much more...

Target Market(s)

Residential Home Renovation, Kitchen and Bath Renovation, Home Improvement

Industry/Entity Type

Residential Construction

Number of Pages Required

5+ page

Font styles to use
Sans Serif
Script

Requirements
Must have
• Similar to Nestlyra.com, except for Braylen At Hearth.
• Must be inviting.
• My Services Offered
• A way to reach me or contact me for estimates with some sort of Screening Questionare.
Nice to have
• Inviting Colors
Should not have
• Not sure at this time

```html
<!DOCTYPE html>
<html lang="en">
<head>
<meta charset="utf-8">
<title>Braylen At Hearth – Home Renovation</title>
<link href="https://fonts.googleapis.com/css2?family=Oswald:wght@400;500;700&family=Open+Sans:wght@400;600;700&display=swap" rel="stylesheet">
<style>
:root{
  --blue:#29a7e1;
  --blue-dark:#1b8bc0;
  --yellow:#f6c31b;
  --dark:#2a2a2a;
  --darker:#1e1e1e;
  --ink:#333;
  --muted:#777;
  --line:#e3e3e3;
  --white:#fff;
}
*{margin:0;padding:0;box-sizing:border-box}
html,body{width:1200px;height:3100px;overflow:hidden}
body{font-family:"Open Sans",Arial,sans-serif;color:var(--ink);background:var(--white);font-size:15px}
h1,h2,h3,.btn,.nav a,.label{font-family:"Oswald","Arial Narrow",sans-serif}
.wrap{width:1040px;margin:0 auto;position:relative}

/* header */
.header{height:208px;position:relative;background:var(--white)}
.topbar{position:absolute;left:420px;right:0;top:0;height:96px;background:var(--blue);clip-path:polygon(40px 0,100% 0,100% 100%,0 100%)}
.brand{position:absolute;left:80px;top:14px;display:flex;align-items:center;gap:14px}
.brand-mark{width:58px;height:58px;background:var(--blue)}
.brand-name{font-family:"Oswald",sans-serif;font-weight:700;font-size:34px;color:var(--dark);line-height:1}
.brand-tag{font-size:11px;color:var(--muted);letter-spacing:1px;margin-top:6px}
.contact-top{position:absolute;top:22px;left:680px;color:var(--white);font-size:13px;line-height:22px}
.contact-top.addr{left:900px}
.contact-top svg{vertical-align:-2px;margin-right:6px}
.socials{position:absolute;right:80px;top:112px;display:flex;gap:8px}
.socials span{width:30px;height:30px;background:var(--yellow);display:block}
.socials span::after{content:"";display:block;width:10px;height:10px;border-radius:50%;background:var(--white);margin:10px}
.nav{position:absolute;left:80px;right:80px;top:162px;display:flex;gap:34px;border-bottom:1px solid var(--line);height:40px}
.nav a{font-size:14px;font-weight:500;color:var(--ink);text-decoration:none;letter-spacing:.5px;padding-top:8px}
.nav a.active{color:var(--blue);border-bottom:3px solid var(--blue)}

/* hero */
.hero{height:512px;position:relative;background:linear-gradient(120deg,#3c2a1c,#6e4c2e 45%,#4a3522);text-align:center;color:var(--white)}
.hero::after{content:"";position:absolute;inset:0;background:rgba(0,0,0,.35)}
.hero-inner{position:relative;z-index:1;padding-top:130px}
.hero h1{font-size:62px;font-weight:700;letter-spacing:2px}
.hero .band{display:inline-block;background:var(--yellow);color:var(--dark);font-family:"Oswald",sans-serif;font-size:28px;font-weight:500;padding:4px 26px;margin-top:8px;letter-spacing:1px}
.btn{display:inline-flex;align-items:center;background:var(--yellow);color:var(--dark);font-size:14px;font-weight:500;letter-spacing:1px;height:42px;padding-left:26px;text-decoration:none}
.btn .arr{width:40px;height:42px;background:var(--dark);margin-left:22px;display:flex;align-items:center;justify-content:center}
.hero .btn{margin-top:48px}

/* cad */
.cad{height:400px;padding-top:48px}
.cad .wrap{display:flex;gap:48px}
.cad-text{width:500px}
h2{font-size:30px;font-weight:500;color:var(--dark);letter-spacing:1px;margin-bottom:16px}
.cad h2{font-size:24px}
p{font-size:13px;line-height:21px;color:var(--muted);margin-bottom:14px}
.cad-photo{width:492px}
.photo{background:linear-gradient(135deg,#5a3a22,#a0703f 50%,#d9b27a)}
.cad-photo .photo{height:250px}
.caption{background:var(--yellow);color:var(--dark);font-family:"Oswald",sans-serif;font-size:14px;text-align:center;height:40px;line-height:40px;letter-spacing:.5px}

/* services */
.services{height:640px}
.services .lead{font-size:13px;color:var(--muted);margin-bottom:30px}
.grid{display:grid;grid-template-columns:repeat(3,1fr);gap:22px 26px}
.card .photo{height:150px}
.card .label{background:var(--blue);color:var(--white);font-size:18px;font-weight:500;height:44px;line-height:44px;padding-left:20px;letter-spacing:.5px}
.center{text-align:center}
.services .btn{margin-top:34px}

/* projects */
.projects{height:430px;background:var(--dark);padding-top:34px;color:var(--white);position:relative}
.projects h2{color:var(--white);margin-bottom:6px}
.projects .lead{font-size:13px;color:#bbb;margin-bottom:22px}
.pair{display:flex;gap:16px}
.pair figure{flex:1}
.pair .photo{height:210px}
.pair .before{background:linear-gradient(135deg,#6b6256,#9b8f7a 60%,#c9bda3)}
.pair .after{background:linear-gradient(135deg,#3a2818,#7a5230 55%,#b88a55)}
.pair .tag{background:var(--yellow);color:var(--dark);font-family:"Oswald",sans-serif;font-size:14px;height:34px;line-height:34px;padding-left:16px}
.slide-arrow{position:absolute;top:250px;width:34px;height:34px;border-radius:50%;background:#555;display:flex;align-items:center;justify-content:center}
.slide-arrow.prev{left:44px}.slide-arrow.next{right:44px}

/* testimonial */
.testimonial{height:360px;padding-top:36px}
.testimonial .lead{font-size:13px;color:var(--muted);margin-bottom:26px}
.quote{border:1px solid var(--line);padding:26px 30px 26px 90px;position:relative}
.quote::before{content:"\201C";position:absolute;left:28px;top:4px;font-size:80px;color:var(--yellow);font-family:Georgia,serif}
.quote p{font-size:15px;line-height:24px;color:#666;margin:0}
.client{display:flex;align-items:center;gap:14px;margin-top:22px}
.avatar{width:54px;height:54px;background:linear-gradient(#c8c8c8,#9a9a9a)}
.client b{display:block;font-size:15px;color:var(--dark)}
.client small{font-size:12px;color:var(--muted)}

/* footer */
.footer{height:420px;background:var(--dark);position:relative}
.footer-info{position:absolute;left:120px;top:50px;color:#ccc;font-size:13px}
.footer-info h3{color:var(--yellow);font-size:18px;font-weight:500;margin-bottom:26px}
.footer-info .row{display:flex;gap:12px;margin-bottom:22px;line-height:20px}
.footer-info .row svg{flex:none;margin-top:3px}
.footer-info b{color:var(--white);font-weight:600}
.quote-form{position:absolute;left:440px;top:-14px;width:300px;background:var(--yellow);padding:20px 34px 30px}
.quote-form h3{font-size:22px;font-weight:500;color:var(--dark);text-align:center;margin-bottom:18px}
.field{font-size:12px;color:var(--dark);border-bottom:1px solid rgba(0,0,0,.35);height:40px;line-height:50px}
.field.msg{height:90px}
.quote-form .submit{display:inline-block;background:var(--white);color:var(--dark);font-family:"Oswald",sans-serif;font-size:13px;padding:8px 26px;margin-top:22px;clip-path:polygon(0 0,100% 0,88% 100%,0 100%)}
.map{position:absolute;left:748px;right:0;top:0;bottom:0;background:linear-gradient(135deg,#d9d9d9,#eeeeee 50%,#cfcfcf)}

/* newsletter */
.newsletter{height:120px;background:var(--darker);position:relative}
.newsletter h3{position:absolute;left:120px;top:32px;color:var(--white);font-size:24px;line-height:28px;font-weight:500;letter-spacing:1px}
.newsletter .email{position:absolute;left:508px;top:44px;width:360px;height:40px;background:#8a8a8a;color:#ddd;font-size:12px;line-height:40px;padding-left:14px}
.newsletter .go{position:absolute;left:868px;top:44px;width:130px;height:40px;background:var(--yellow);font-family:"Oswald",sans-serif;font-size:13px;text-align:center;line-height:40px;color:var(--dark)}
.copy{height:40px;background:#141414;color:#888;font-size:11px;display:flex;align-items:center;justify-content:space-between;padding:0 120px}
.copy .icons{display:flex;gap:14px}
.copy .icons i{width:10px;height:10px;border-radius:50%;background:#888;display:block}
</style>
</head>
<body>

<header class="header">
  <div class="topbar"></div>
  <div class="brand">
    <span class="brand-mark"></span>
    <div>
      <div class="brand-name">Braylen At Hearth</div>
      <div class="brand-tag">DESIGN, BUILD &amp; REMODELING CONTRACTORS</div>
    </div>
  </div>
  <div class="contact-top">
    <div><svg width="12" height="12" viewBox="0 0 12 12"><path d="M2 1h3l1 3-2 1a7 7 0 0 0 3 3l1-2 3 1v3c-6 0-9-3-9-9z" fill="#fff"/></svg>+1 (555) 014-2290</div>
    <div><svg width="12" height="12" viewBox="0 0 12 12"><rect x="1" y="2" width="10" height="8" fill="none" stroke="#fff"/><path d="M1 2l5 4 5-4" fill="none" stroke="#fff"/></svg>info@braylenathearth.com</div>
  </div>
  <div class="contact-top addr">
    <div><svg width="12" height="12" viewBox="0 0 12 12"><path d="M6 11S2 7 2 4.5a4 4 0 0 1 8 0C10 7 6 11 6 11z" fill="#fff"/></svg>48 Kestrel Lane</div>
    <div>Ridgewell, Hearth County</div>
  </div>
  <div class="socials"><span></span><span></span><span></span><span></span></div>
  <nav class="nav">
    <a class="active" href="#">HOME</a><a href="#">ABOUT</a><a href="#">PROJECTS</a><a href="#">SERVICES</a><a href="#">3D CAD DESIGNS</a><a href="#">TESTIMONIALS</a><a href="#">GALLERY</a><a href="#">GET A QUOTE</a><a href="#">CONTACT</a>
  </nav>
</header>

<section class="hero" role="img" aria-label="Warm wooden kitchen interior with cabinets and pendant lights">
  <div class="hero-inner">
    <h1>DESIGNING- CREATION- MAKING</h1>
    <div class="band">WE MAKE YOUR HOME BEAUTIFUL</div><br>
    <a class="btn" href="#">GET A QUOTE NOW<span class="arr"><svg width="10" height="12" viewBox="0 0 10 12"><path d="M1 0l8 6-8 6z" fill="#fff"/></svg></span></a>
  </div>
</section>

<section class="cad">
  <div class="wrap">
    <div class="cad-text">
      <h2>3D CAD DESIGN PREVIEW</h2>
      <p>If you want to see the preview of the renovation of your room, kitchen, bath, and more, just tell us your requirements. We will make the 3D CAD design based on your room dimensions and your requirements. So you will have a clear idea how your room will look like before any work begins on your project.</p>
      <p>To make a 3D CAD design we just need the room dimensions, some images and anything you want in the final look of your space.</p>
      <p>There is always a free quote from our <b style="color:#333">experts</b>.</p>
      <a class="btn" href="#">ASK FOR 3D CAD DESIGN<span class="arr"><svg width="10" height="12" viewBox="0 0 10 12"><path d="M1 0l8 6-8 6z" fill="#fff"/></svg></span></a>
    </div>
    <div class="cad-photo">
      <div class="photo" role="img" aria-label="3D rendered kitchen with wooden cabinets and pendant lights"></div>
      <div class="caption">3D CAD DESIGN FOR KITCHEN</div>
    </div>
  </div>
</section>

<section class="services">
  <div class="wrap">
    <h2>OUR SERVICES</h2>
    <p class="lead">From: Custom Carpentry &amp; Finishes, Kitchens, Baths, Basements, Decks, Porches, Whole House Renovation – Skilled Craftsmanship (Hardwood Flooring, Floor and Wall Tile) and much more...</p>
    <div class="grid">
      <div class="card"><div class="photo" role="img" aria-label="Worker renovating a room"></div><div class="label">RENOVATION</div></div>
      <div class="card"><div class="photo" role="img" aria-label="Plumber fitting pipes under a sink" style="background:linear-gradient(135deg,#8b8f94,#c9ccd0)"></div><div class="label">PLUMBING</div></div>
      <div class="card"><div class="photo" role="img" aria-label="Painter rolling paint on a wall" style="background:linear-gradient(135deg,#c9c3b6,#efece4)"></div><div class="label">PAINTING</div></div>
      <div class="card"><div class="photo" role="img" aria-label="Electrician working on wiring" style="background:linear-gradient(135deg,#bfbab2,#e8e4dc)"></div><div class="label">ELECTRICAL</div></div>
      <div class="card"><div class="photo" role="img" aria-label="Brick wall being laid" style="background:linear-gradient(135deg,#8d3f24,#c7673e)"></div><div class="label">WALLS</div></div>
      <div class="card"><div class="photo" role="img" aria-label="Red tiled roof" style="background:linear-gradient(135deg,#9a3a22,#d46a3e)"></div><div class="label">ROOFING</div></div>
    </div>
    <div class="center"><a class="btn" href="#">MORE JOBS<span class="arr"><svg width="10" height="12" viewBox="0 0 10 12"><path d="M1 0l8 6-8 6z" fill="#fff"/></svg></span></a></div>
  </div>
</section>

<section class="projects">
  <div class="wrap">
    <h2>OUR PROJECTS</h2>
    <p class="lead">Please check all kind of works we done in recent past and decide that we are the best ones for your projects.</p>
    <div class="pair">
      <figure><div class="photo before" role="img" aria-label="Kitchen before renovation"></div><div class="tag">BEFORE</div></figure>
      <figure><div class="photo after" role="img" aria-label="Kitchen after renovation"></div><div class="tag">AFTER</div></figure>
    </div>
  </div>
  <span class="slide-arrow prev"><svg width="10" height="12" viewBox="0 0 10 12"><path d="M9 0L1 6l8 6z" fill="#fff"/></svg></span>
  <span class="slide-arrow next"><svg width="10" height="12" viewBox="0 0 10 12"><path d="M1 0l8 6-8 6z" fill="#fff"/></svg></span>
</section>

<section class="testimonial">
  <div class="wrap">
    <h2>CLIENTS TESTIMONIAL</h2>
    <p class="lead">Check all our clients say about our work, quality and dedication.</p>
    <div class="quote"><p>The crew came out to do a few odd jobs and did great work. Fixed a window, a sink and an outlet all for a fair price. I am happy with the work and the service. I would surely use them again.</p></div>
    <div class="client"><div class="avatar" role="img" aria-label="Client portrait"></div><div><b>Delia Marren</b><small>Homeowner, Ridgewell</small></div></div>
  </div>
</section>

<footer class="footer">
  <div class="footer-info">
    <h3>RIDGEWELL</h3>
    <div class="row"><svg width="12" height="14" viewBox="0 0 12 14"><path d="M6 13S1 8 1 5a5 5 0 0 1 10 0c0 3-5 8-5 8z" fill="#f6c31b"/></svg><div>Address:<br><b>12 Harbor Row, Ridgewell</b></div></div>
    <div class="row"><svg width="12" height="14" viewBox="0 0 12 12"><path d="M2 1h3l1 3-2 1a7 7 0 0 0 3 3l1-2 3 1v3c-6 0-9-3-9-9z" fill="#f6c31b"/></svg><div>Phone:<br><b>+1 (555) 014-2291</b></div></div>
    <div class="row"><svg width="12" height="14" viewBox="0 0 12 12"><rect x="1" y="2" width="10" height="8" fill="none" stroke="#f6c31b"/><path d="M1 2l5 4 5-4" fill="none" stroke="#f6c31b"/></svg><div>Email:<br><b>contact@braylenathearth.com</b></div></div>
  </div>
  <div class="quote-form">
    <h3>REQUEST A QUOTE</h3>
    <div class="field">Name</div>
    <div class="field">Email</div>
    <div class="field">Phone</div>
    <div class="field msg">Message</div>
    <span class="submit">SUBMIT</span>
  </div>
  <div class="map" role="img" aria-label="Street map showing the office location"></div>
</footer>

<section class="newsletter">
  <h3>LIKE OUR WORK?<br>RECEIVE OUR EMAIL NEWSLETTER</h3>
  <div class="email">Enter your email</div>
  <div class="go">SUBSCRIBE</div>
</section>
<div class="copy"><span>© ALL RIGHTS RESERVED · BRAYLENATHEARTH.COM</span><span class="icons"><i></i><i></i><i></i><i></i><i></i></span></div>

</body>
</html>
```